Recreating a Opt-in for a FREE BOOK for brides.

I need to have an opt-in box recreated to make brides want to get my free book. The opt-in message is already on the mock website. It needs to look graphically pleasing in the colors being used, but bold enough to grab the viewers attention. I am including the link to the website where the graphic needs to be re-created. You'll notice there are two areas where the graphics need to go.

Target Market(s)

Brides

Requirements
Must have
• Begin by looking at the website..http://qvotrl.com/zu-pim/
On the homepage is the current "A Gift For You" graphic. (I have included an image of the home page for the circled area that needs to be recreated.) As of now, the graphics looks amateurish. It needs your professional upgrade. The image of the book has also been uploaded as a file for you to use.

In addition, on the FAQ page, there is a graphic that has been created to fit that area of the page to get the book (circled area of the graphic has been uploaded). I need to have the same graphic you are creating for the home page, but adjust it to be placed on this page. When you recreate the graphic for the FAQ page, there are 2 changes to the text:

1. Change the word "Receive" to "Download." (The rest of the sentence should stay the same.)
2. Delete the entire sentence "Or, pay $17.95 at zellora or tolliver and wrenfield by clicking here.
Nice to have
• Normal file formats such as jpeg, photoshop or ai are fine.

```html
<!DOCTYPE html>
<html lang="en">
<head>
<meta charset="utf-8">
<title>A Gift For You – Free Bride's Guide</title>
<link rel="stylesheet" href="https://fonts.googleapis.com/css2?family=Montserrat:wght@700;800&family=Mulish:wght@300;400;800&display=swap">
<style>
  :root {
    --sky: #cdeef2;
    --sky-light: #dcf4f6;
    --frame: rgba(255, 255, 255, 0.7);
    --teal: #2e7b80;
    --teal-deep: #1f5f66;
    --tan: #d8ae8e;
    --ink: #141414;
  }
  * { margin: 0; padding: 0; box-sizing: border-box; }
  html, body { width: 1200px; height: 900px; overflow: hidden; }
  body {
    background: radial-gradient(ellipse at 40% 40%, var(--sky-light), var(--sky) 75%);
    font-family: "Mulish", sans-serif;
    color: var(--ink);
    position: relative;
  }
  .offer-frame {
    position: absolute;
    left: 58px; top: 72px;
    width: 733px; height: 766px;
    border: 10px solid var(--frame);
    background: rgba(255, 255, 255, 0.12);
  }
  .headline { position: absolute; left: 0; top: 0; width: 800px; height: 380px; }
  .headline-a, .headline-gift, .headline-for-you {
    position: absolute;
    font-family: "Montserrat", sans-serif;
    font-weight: 800;
    line-height: 1;
    white-space: nowrap;
  }
  .headline-a { left: 157px; top: 165px; font-size: 86px; color: var(--teal); }
  .headline-gift { left: 236px; top: 143px; font-size: 168px; color: var(--tan); letter-spacing: -6px; }
  .headline-for-you { left: 260px; top: 307px; font-size: 64px; color: var(--teal); letter-spacing: -2px; }
  .book-title {
    position: absolute; left: 0; top: 397px; width: 794px;
    text-align: center;
  }
  .book-title-lead {
    font-weight: 300; font-size: 35px; line-height: 36px; color: var(--ink);
  }
  .book-title-main {
    margin-top: 14px;
    font-family: "Montserrat", sans-serif;
    font-weight: 800; font-size: 62px; line-height: 1;
    color: var(--teal); letter-spacing: -3px;
  }
  .download-button {
    position: absolute; left: 249px; top: 591px;
    width: 275px; height: 59px; border-radius: 30px;
    background: var(--tan);
    display: flex; align-items: center; justify-content: center;
    font-family: "Montserrat", sans-serif; font-weight: 800;
    font-size: 27px; letter-spacing: 4px; color: var(--teal-deep);
    text-decoration: none;
  }
  .free-copy {
    position: absolute; left: 0; top: 664px; width: 784px;
    text-align: center; font-size: 33px; font-weight: 400;
  }
  .free-copy strong { font-weight: 800; }
  .readership {
    position: absolute; left: 0; top: 739px; width: 784px;
    text-align: center; font-size: 19px; letter-spacing: 0.5px;
  }
  .book-visual { position: absolute; left: 700px; top: 125px; width: 430px; height: 645px; }
</style>
</head>
<body>
  <div class="offer-frame"></div>

  <div class="headline">
    <span class="headline-a">A</span>
    <span class="headline-gift">GIFT</span>
    <span class="headline-for-you">FOR YOU!</span>
  </div>

  <div class="book-title">
    <p class="book-title-lead">The Essential Bride’s Guide<br>For Choosing A</p>
    <p class="book-title-main">WEDDING CAKE</p>
  </div>

  <a class="download-button" href="#">DOWNLOAD</a>
  <p class="free-copy">Your <strong>FREE COPY</strong> Now!</p>
  <p class="readership">Read By Over 550,000 Brides</p>

  <svg class="book-visual" viewBox="0 0 430 645" role="img" aria-label="Hardcover bridal guidebook, cover showing a kissing bridal couple behind a tiered white cake with a pink rose">
    <defs>
      <linearGradient id="coverTone" x1="0" y1="0" x2="1" y2="1">
        <stop offset="0" stop-color="#f4f1ea"/>
        <stop offset="0.45" stop-color="#efe3dc"/>
        <stop offset="0.75" stop-color="#bfe0e0"/>
        <stop offset="1" stop-color="#eef2f0"/>
      </linearGradient>
    </defs>
    <polygon points="6,22 416,8 410,588 12,637" fill="url(#coverTone)"/>
    <polygon points="6,22 38,20 44,634 12,637" fill="#f7f7f5"/>
  </svg>
</body>
</html>
```